Building Servicess

We need a new business card design for a company. We specialise in: Electrical/Site temporary electrics, Data/Network Installation, Passive Fire Protection

Industry/Entity Type

Construction

Contact Information for Business Card

Services provided as detailed on project description

Font styles to use
Serif

Colors
0054AA
0677BA
7BADD7
CADEEF
E8F1F8
00AB8E
00BBA5
67D7C9
C6EFE9
E9F9F6
EB3D1F
EC4F4E
F09395
F8D3D4
FCEDEE

Requirements
Must have
• Company logo-contact details-phone numbers

```html
<!DOCTYPE html>
<html lang="en">
<head>
<meta charset="utf-8">
<title>Vantor Site Services – Business Card</title>
<link href="https://fonts.googleapis.com/css2?family=Montserrat:wght@500&family=Oswald:wght@400;500&display=swap" rel="stylesheet">
<style>
  :root {
    --brand-blue: #0677BA;
    --deep-blue: #0054AA;
    --mid-blue: #7BADD7;
    --pale-blue: #E8F1F8;
    --soft-grey: #EEEEF0;
    --line-grey: #808086;
    --text-grey: #8A8A90;
    --card-white: #FFFFFF;
    --stage: #3C3D41;
  }
  * { margin: 0; padding: 0; box-sizing: border-box; }
  html, body { width: 1200px; height: 900px; overflow: hidden; }
  body {
    background: var(--stage);
    font-family: "Oswald", "Arial Narrow", sans-serif;
    position: relative;
  }
  .card {
    position: absolute;
    left: 280px;
    width: 640px;
    height: 366px;
    background: var(--card-white);
    border-radius: 14px;
    overflow: hidden;
    box-shadow: 0 14px 30px rgba(0,0,0,.35);
  }
  .card--front { top: 64px; }
  .card--back { top: 470px; }

  .backdrop {
    position: absolute;
    inset: 0;
    background: linear-gradient(115deg, var(--pale-blue) 0%, var(--soft-grey) 35%, var(--card-white) 60%, var(--pale-blue) 100%);
    opacity: .75;
  }
  .card--back .backdrop {
    inset: auto 0 0 0;
    height: 210px;
    right: 90px;
    background: linear-gradient(100deg, var(--pale-blue) 0%, var(--soft-grey) 45%, rgba(255,255,255,0) 100%);
    opacity: .8;
  }

  .brand {
    position: absolute;
    display: flex;
    flex-direction: column;
    align-items: center;
  }
  .brand__row { display: flex; align-items: center; gap: 12px; }
  .brand__mark { width: 26px; height: 26px; background: var(--brand-blue); }
  .brand__name {
    font-family: "Montserrat", sans-serif;
    font-weight: 500;
    color: var(--brand-blue);
    font-size: 30px;
    letter-spacing: 1px;
    white-space: nowrap;
  }
  .brand__rule { margin-top: 8px; height: 2px; background: var(--line-grey); width: 92%; }
  .card--front .brand { left: 0; right: 0; top: 118px; }
  .card--back .brand { left: 60px; right: 120px; top: 76px; }
  .card--back .brand__name { font-size: 26px; }

  .services-band {
    position: absolute;
    left: 0; right: 0;
    top: 256px;
    height: 40px;
    background: linear-gradient(90deg, var(--deep-blue), var(--brand-blue));
    color: var(--card-white);
    font-weight: 500;
    font-size: 15.5px;
    display: flex;
    align-items: center;
    justify-content: center;
    gap: 10px;
    letter-spacing: .2px;
  }
  .services-band .divider { opacity: .9; }

  .side-stripe {
    position: absolute;
    top: 0; bottom: 0; right: 0;
    width: 62px;
    background: var(--brand-blue);
  }
  .side-line {
    position: absolute;
    top: 0; bottom: 0;
    width: 3px;
    background: var(--line-grey);
  }
  .side-line--outer { right: 80px; }
  .side-line--inner { right: 71px; }

  .contact-person {
    position: absolute;
    left: 70px;
    top: 178px;
  }
  .contact-person__name { color: var(--brand-blue); font-size: 24px; font-weight: 500; line-height: 1.1; }
  .contact-person__role { color: var(--text-grey); font-size: 16px; margin-left: 14px; margin-top: 2px; }

  .contact-list { position: absolute; list-style: none; }
  .contact-list li {
    display: flex;
    align-items: center;
    gap: 9px;
    color: var(--text-grey);
    font-size: 17px;
    line-height: 1.55;
  }
  .contact-list svg { width: 18px; height: 18px; flex: none; fill: var(--brand-blue); }
  .contact-list--phones { left: 84px; top: 250px; }
  .contact-list--web { left: 300px; top: 196px; }

  .address {
    position: absolute;
    left: 70px;
    bottom: 22px;
    color: var(--text-grey);
    font-size: 16px;
    white-space: nowrap;
  }
</style>
</head>
<body>

<section class="card card--front" aria-label="Business card front">
  <div class="backdrop" role="img" aria-label="Soft blue and grey background wash"></div>
  <div class="brand">
    <div class="brand__row">
      <span class="brand__mark"></span>
      <span class="brand__name">VANTOR SITE SERVICES LTD</span>
    </div>
    <div class="brand__rule"></div>
  </div>
  <div class="services-band">
    <span>Electrical/Site Temporary Electrics</span><span class="divider">|</span>
    <span>Data/Network Installation</span><span class="divider">|</span>
    <span>Passive Fire Protection</span>
  </div>
</section>

<section class="card card--back" aria-label="Business card back">
  <div class="backdrop" role="img" aria-label="Soft blue and grey background wash"></div>
  <div class="side-line side-line--outer"></div>
  <div class="side-line side-line--inner"></div>
  <div class="side-stripe"></div>

  <div class="brand">
    <div class="brand__row">
      <span class="brand__mark"></span>
      <span class="brand__name">VANTOR SITE SERVICES LTD</span>
    </div>
    <div class="brand__rule"></div>
  </div>

  <div class="contact-person">
    <p class="contact-person__name">Your Name Goes Here</p>
    <p class="contact-person__role">Your Position</p>
  </div>

  <ul class="contact-list contact-list--phones">
    <li>
      <svg viewBox="0 0 24 24" aria-hidden="true"><path d="M7 1h10a2 2 0 0 1 2 2v18a2 2 0 0 1-2 2H7a2 2 0 0 1-2-2V3a2 2 0 0 1 2-2zm0 4v13h10V5H7zm5 14.5a1.2 1.2 0 1 0 0 2.4 1.2 1.2 0 0 0 0-2.4z"/></svg>
      <span>12345 678901</span>
    </li>
    <li>
      <svg viewBox="0 0 24 24" aria-hidden="true"><path d="M3 8c3-3 15-3 18 0l-1 3-4-1V8c-2-.6-6-.6-8 0v2l-4 1zM6 13h12l2 8H4zm6 1.8a2.6 2.6 0 1 0 0 5.2 2.6 2.6 0 0 0 0-5.2z"/></svg>
      <span>12345 678901</span>
    </li>
  </ul>

  <ul class="contact-list contact-list--web">
    <li>
      <svg viewBox="0 0 24 24" aria-hidden="true"><path d="M2 5h20v14H2zm2 2v.5l8 5.5 8-5.5V7zm0 3v7h16v-7l-8 5.5z"/></svg>
      <span>yourmail@mail.com</span>
    </li>
    <li>
      <svg viewBox="0 0 24 24" aria-hidden="true"><path d="M12 2a10 10 0 1 0 0 20 10 10 0 0 0 0-20zm0 2c1.3 1.5 2.2 3.6 2.4 7h-4.8c.2-3.4 1.1-5.5 2.4-7zM9.6 4.4C8.6 6.2 7.8 8.4 7.6 11H4.1a8 8 0 0 1 5.5-6.6zm4.8 0A8 8 0 0 1 19.9 11h-3.5c-.2-2.6-1-4.8-2-6.6zM4.1 13h3.5c.2 2.6 1 4.8 2 6.6A8 8 0 0 1 4.1 13zm5.5 0h4.8c-.2 3.4-1.1 5.5-2.4 7-1.3-1.5-2.2-3.6-2.4-7zm6.8 0h3.5a8 8 0 0 1-5.5 6.6c1-1.8 1.8-4 2-6.6z"/></svg>
      <span>www.website.com</span>
    </li>
  </ul>

  <p class="address">Vantor Site Services Ltd. Harlow Road, Brentwood, Essex, CM14 2QT.</p>
</section>

</body>
</html>
```